Menu Design Project

We are Tinroof Delivery a multiple restaurant delivery service. I am looking for a tri-fold, take out style menu. On the front, at the TOP I would like the menu to say "WE DELIVER!" There will be 4 restaurants that I am promoting, so each restaurant will have 1 panel in the menu.
The back of the tri-fold should incorporate an area for postage and address, since i will be mailing these pieces. Also on the back there should be the ordering instructions that will be included in the files.
I would like for the front to have either pictures of food, the logos of the restaurants, our logo, or a combination of the three. Menu items and prices will be input by me. We just need a template designed.

Size= 11" X 17"
We are looking to make a decision today or tomorrow at the latest.

Restaurant

• We are mailing these through whole route flyer drop. Must have an area for address label and postage.

"We Deliver" on front of tri-fold, at the top.
• Do not use all of the food picks(Unless it looks Awesome). The files are so that you have the options of food picks

```html
<!DOCTYPE html>
<html lang="en">
<head>
<meta charset="utf-8">
<title>Tinroof Delivery – Tri-fold Menu Template</title>
<link rel="stylesheet" href="https://fonts.googleapis.com/css2?family=Alegreya+Sans:ital,wght@0,400;0,700;0,800;1,700;1,800&display=swap">
<style>
:root{
  --red:#b01e24;
  --deep-red:#8c151a;
  --pill:#6e0c10;
  --dark:#262223;
  --ink:#231f20;
  --paper:#ffffff;
  --cream:#eee7dc;
  --muted:#8b8584;
  --line:#9a9a9a;
  --font:"Alegreya Sans", Arial, sans-serif;
}
*{box-sizing:border-box;margin:0;padding:0}
html,body{width:920px;height:1200px;overflow:hidden;background:#fff;font-family:var(--font)}
.sheet{position:absolute;left:24px;width:862px;height:558px;background:var(--paper);box-shadow:0 2px 8px rgba(0,0,0,.35);overflow:hidden}
.sheet--outside{top:22px}
.sheet--inside{top:602px}
.panel{position:absolute;top:0;height:558px;overflow:hidden}
.panel--left{left:0;width:289px}
.panel--middle{left:289px;width:284px}
.panel--right{left:573px;width:289px}
.photo{position:absolute}
.band-red{position:absolute;left:0;width:100%}
.menu-title{position:absolute;left:25px;font-weight:800;font-style:italic;font-size:21px;letter-spacing:-.3px;color:#fff}
.menu-title--grey{color:#6f6b6b}
.menu-section{position:absolute;left:14px;width:262px}
.menu-section__head{display:inline-block;height:15px;width:128px;border-radius:8px;background:var(--pill);color:#fff;font-size:8.5px;font-weight:700;line-height:15px;padding-left:20px;text-transform:uppercase}
.items{display:grid;grid-template-columns:76px 51px 76px 40px;padding-left:22px;margin-top:10px;font-size:7px;line-height:6.8px;color:#fff;font-weight:700}
.items span:nth-child(even){font-weight:400;opacity:.85}
.items--grey{color:#7a7474}
.footer-strip{position:absolute;left:0;top:526px;width:100%;height:32px;background:#fff;display:flex;align-items:center;padding-left:8px;gap:12px}
.brand-mini{display:flex;align-items:center;gap:3px;color:var(--red);font-size:9px;font-weight:800;line-height:1}
.brand-mini__dot{width:8px;height:8px;border-radius:50%;background:var(--red)}
.tagline{font-style:italic;font-weight:800;font-size:12px;color:var(--red)}
.logo-box{position:absolute;display:flex;align-items:center;justify-content:center;text-align:center;font-weight:700;line-height:1.05}
.call-line{font-size:12.5px;font-weight:700;color:#fff;letter-spacing:.2px}
.call-line b{color:var(--red);letter-spacing:1px}
</style>
</head>
<body>

<!-- OUTSIDE SHEET -->
<section class="sheet sheet--outside">

  <!-- Restaurant panel: Saffron Court -->
  <div class="panel panel--left">
    <div class="photo" role="img" aria-label="Indian samosas and tandoori chicken on a platter" style="left:0;top:0;width:289px;height:112px;background:linear-gradient(120deg,#c98b3a,#9c4a1e 55%,#6b7a3a)"></div>
    <div class="photo" role="img" aria-label="Bowl of sweet dumplings" style="left:110px;top:112px;width:80px;height:58px;background:linear-gradient(135deg,#f2ede6,#b8702e)"></div>
    <div class="photo" role="img" aria-label="Curry served in a bowl" style="left:190px;top:112px;width:99px;height:58px;background:linear-gradient(135deg,#8a5a2c,#c2762d)"></div>
    <div class="logo-box" style="left:10px;top:112px;width:98px;height:38px;background:#111;color:#fff;font-size:12px">Saffron Court</div>
    <svg class="band-red" style="top:164px;height:362px" width="289" height="362" viewBox="0 0 289 362" aria-hidden="true"><path d="M0 12 Q150 -4 289 8 L289 362 L0 362Z" fill="var(--red)"/></svg>
    <div class="photo" role="img" aria-label="Faint outline drawing of chillies" style="left:150px;top:330px;width:120px;height:190px;background:linear-gradient(180deg,rgba(255,255,255,0),rgba(255,255,255,.07))"></div>
    <h2 class="menu-title" style="top:180px">Choose your menu</h2>
    <div class="menu-section" style="top:210px"><div class="menu-section__head">Choose your curry</div>
      <div class="items"><span>Beef Pizza</span><span>$ 12.</span><span>Beef Pizza</span><span>$ 12.</span><span>Margherita</span><span>$ 12.</span><span>Margherita</span><span>$ 12.</span><span>Chicken supreme</span><span>$ 12.</span><span>Chicken supreme</span><span>$ 12.</span><span>Beef Pizza</span><span>$ 12.</span><span>Beef Pizza</span><span>$ 12.</span><span>Margherita</span><span>$ 12.</span><span>Margherita</span><span>$ 12.</span></div></div>
    <div class="menu-section" style="top:277px"><div class="menu-section__head">Choose your pasta</div>
      <div class="items"><span>Beef Pizza</span><span>$ 12.</span><span>Beef Pizza</span><span>$ 12.</span><span>Margherita</span><span>$ 12.</span><span>Margherita</span><span>$ 12.</span><span>Chicken supreme</span><span>$ 12.</span><span>Chicken supreme</span><span>$ 12.</span><span>Beef Pizza</span><span>$ 12.</span><span>Beef Pizza</span><span>$ 12.</span><span>Margherita</span><span>$ 12.</span><span>Margherita</span><span>$ 12.</span></div></div>
    <div class="menu-section" style="top:349px"><div class="menu-section__head">Choose your pasta</div>
      <div class="items"><span>Beef Pizza</span><span>$ 12.</span><span>Beef Pizza</span><span>$ 12.</span><span>Margherita</span><span>$ 12.</span><span>Margherita</span><span>$ 12.</span><span>Chicken supreme</span><span>$ 12.</span><span>Chicken supreme</span><span>$ 12.</span><span>Beef Pizza</span><span>$ 12.</span><span>Beef Pizza</span><span>$ 12.</span><span>Margherita</span><span>$ 12.</span><span>Margherita</span><span>$ 12.</span></div></div>
    <div class="menu-section" style="top:419px"><div class="menu-section__head">Choose your pasta</div>
      <div class="items"><span>Beef Pizza</span><span>$ 12.</span><span>Beef Pizza</span><span>$ 12.</span><span>Margherita</span><span>$ 12.</span><span>Margherita</span><span>$ 12.</span><span>Chicken supreme</span><span>$ 12.</span><span>Chicken supreme</span><span>$ 12.</span><span>Beef Pizza</span><span>$ 12.</span><span>Beef Pizza</span><span>$ 12.</span><span>Margherita</span><span>$ 12.</span><span>Margherita</span><span>$ 12.</span></div></div>
    <div class="footer-strip"><div class="brand-mini"><span class="brand-mini__dot"></span>Tinroof</div><p class="tagline">We Bring Your Favorite Restaurants Right to Your Door!</p></div>
  </div>

  <!-- Mailing panel -->
  <div class="panel panel--middle">
    <div class="mail-area" style="position:absolute;left:17px;top:28px;width:247px;height:380px;border:1px solid var(--line)"></div>
    <div style="position:absolute;left:24px;top:478px;display:flex;align-items:center;gap:5px">
      <span style="width:16px;height:16px;border-radius:50%;background:var(--red)"></span>
      <span style="font-size:19px;font-weight:800;color:var(--red);line-height:.95">Tinroof<br><span style="font-size:10px;letter-spacing:2px">DELIVERY</span></span>
    </div>
    <div style="position:absolute;left:167px;top:483px;color:var(--ink);font-size:9.5px;line-height:11px">
      <div style="color:var(--red);font-weight:800;font-style:italic;font-size:11px">CALL NOW</div>
      <div>(555) 0 food now</div>
      <div>(555) 010-2468</div>
    </div>
  </div>

  <!-- Front cover -->
  <div class="panel panel--right">
    <div class="photo" role="img" aria-label="Slice of lasagne" style="left:0;top:0;width:180px;height:115px;background:linear-gradient(135deg,#2a0d08,#b3401c 55%,#e0a45a)"></div>
    <div class="photo" role="img" aria-label="Glazed ribs" style="left:180px;top:0;width:109px;height:115px;background:linear-gradient(135deg,#4a1a10,#8a3a1c)"></div>
    <div class="photo" role="img" aria-label="Curry dish with herbs" style="left:0;top:115px;width:95px;height:90px;background:linear-gradient(135deg,#6a3a1a,#b05a22)"></div>
    <div class="photo" role="img" aria-label="Toasted sandwich with olive" style="left:95px;top:115px;width:194px;height:90px;background:linear-gradient(135deg,#d9b07a,#8c5a2a 60%,#3a2414)"></div>
    <svg style="position:absolute;left:0;top:170px" width="289" height="60" viewBox="0 0 289 60" aria-hidden="true"><path d="M0 60 L0 40 Q120 0 289 30 L289 60Z" fill="#fff"/></svg>
    <div style="position:absolute;left:0;top:225px;width:289px;text-align:center">
      <span style="display:inline-block;width:34px;height:34px;border-radius:50%;background:var(--red);margin-bottom:6px"></span>
      <div style="font-size:46px;font-weight:800;color:var(--red);line-height:.9">Tinroof</div>
      <div style="font-size:15px;font-weight:800;color:var(--red);letter-spacing:4px">DELIVERY</div>
    </div>
    <svg class="band-red" style="top:335px;height:191px" width="289" height="191" viewBox="0 0 289 191" aria-hidden="true"><path d="M0 20 Q70 0 150 18 Q230 34 289 8 L289 191 L0 191Z" fill="var(--red)"/></svg>
    <div style="position:absolute;right:12px;top:402px;font-size:36px;font-weight:800;font-style:italic;color:#fff">We deliver...</div>
    <div style="position:absolute;left:0;top:526px;width:289px;height:32px;background:var(--dark);display:flex;align-items:center;justify-content:center">
      <p class="call-line"><b>CALL NOW</b> (555) 0 food now (555) 010-2468</p>
    </div>
  </div>
</section>

<!-- INSIDE SHEET -->
<section class="sheet sheet--inside">

  <!-- Restaurant panel: Harbor Slice -->
  <div class="panel panel--left">
    <div class="photo" role="img" aria-label="Pepperoni pizza with peppers" style="left:0;top:0;width:289px;height:112px;background:linear-gradient(120deg,#e0b26a,#b8361c 50%,#5a7a2a)"></div>
    <div class="logo-box" style="left:0;top:112px;width:98px;height:58px;background:#fff;color:var(--red);font-size:15px;font-weight:800">Harbor Slice</div>
    <div class="photo" role="img" aria-label="Layered lasagne" style="left:98px;top:112px;width:93px;height:58px;background:linear-gradient(135deg,#3a120a,#b3401c)"></div>
    <div class="photo" role="img" aria-label="Plate of pasta" style="left:191px;top:112px;width:98px;height:58px;background:linear-gradient(135deg,#2a1a12,#b8542a 60%,#f0e6da)"></div>
    <svg class="band-red" style="top:164px;height:362px" width="289" height="362" viewBox="0 0 289 362" aria-hidden="true"><path d="M0 14 Q150 -4 289 8 L289 362 L0 362Z" fill="var(--red)"/></svg>
    <h2 class="menu-title" style="top:180px">Choose your menu</h2>
    <div class="menu-section" style="top:210px"><div class="menu-section__head">Choose your pizza</div>
      <div class="items"><span>Beef Pizza</span><span>$ 12.</span><span>Beef Pizza</span><span>$ 12.</span><span>Margherita</span><span>$ 12.</span><span>Margherita</span><span>$ 12.</span><span>Chicken supreme</span><span>$ 12.</span><span>Chicken supreme</span><span>$ 12.</span><span>Beef Pizza</span><span>$ 12.</span><span>Beef Pizza</span><span>$ 12.</span><span>Margherita</span><span>$ 12.</span><span>Margherita</span><span>$ 12.</span></div></div>
    <div class="menu-section" style="top:277px"><div class="menu-section__head">Choose your pasta</div>
      <div class="items"><span>Beef Pizza</span><span>$ 12.</span><span>Beef Pizza</span><span>$ 12.</span><span>Margherita</span><span>$ 12.</span><span>Margherita</span><span>$ 12.</span><span>Chicken supreme</span><span>$ 12.</span><span>Chicken supreme</span><span>$ 12.</span><span>Beef Pizza</span><span>$ 12.</span><span>Beef Pizza</span><span>$ 12.</span><span>Margherita</span><span>$ 12.</span><span>Margherita</span><span>$ 12.</span></div></div>
    <div class="menu-section" style="top:349px"><div class="menu-section__head">Choose your pasta</div>
      <div class="items"><span>Beef Pizza</span><span>$ 12.</span><span>Beef Pizza</span><span>$ 12.</span><span>Margherita</span><span>$ 12.</span><span>Margherita</span><span>$ 12.</span><span>Chicken supreme</span><span>$ 12.</span><span>Chicken supreme</span><span>$ 12.</span><span>Beef Pizza</span><span>$ 12.</span><span>Beef Pizza</span><span>$ 12.</span><span>Margherita</span><span>$ 12.</span><span>Margherita</span><span>$ 12.</span></div></div>
    <div class="menu-section" style="top:419px"><div class="menu-section__head">Choose your pasta</div>
      <div class="items"><span>Beef Pizza</span><span>$ 12.</span><span>Beef Pizza</span><span>$ 12.</span><span>Margherita</span><span>$ 12.</span><span>Margherita</span><span>$ 12.</span><span>Chicken supreme</span><span>$ 12.</span><span>Chicken supreme</span><span>$ 12.</span><span>Beef Pizza</span><span>$ 12.</span><span>Beef Pizza</span><span>$ 12.</span><span>Margherita</span><span>$ 12.</span><span>Margherita</span><span>$ 12.</span></div></div>
    <div class="footer-strip"><div class="brand-mini"><span class="brand-mini__dot"></span>Tinroof</div><p class="tagline">We Bring Your Favorite Restaurants Right to Your Door!</p></div>
  </div>

  <!-- Restaurant panel: Ironstone Brewhouse -->
  <div class="panel panel--middle">
    <div class="photo" role="img" aria-label="Faded burger with onion rings as panel background" style="left:0;top:0;width:284px;height:478px;background:linear-gradient(180deg,#f1ede8 0%,#e9e2d8 40%,#d8c8b2 75%,#a88a6a 100%)"></div>
    <h2 class="menu-title menu-title--grey" style="top:20px">Choose your menu</h2>
    <div class="menu-section" style="top:91px"><div class="menu-section__head" style="background:var(--red)">Choose your burger</div>
      <div class="items items--grey"><span>Beef Pizza</span><span>$ 12.</span><span>Beef Pizza</span><span>$ 12.</span><span>Margherita</span><span>$ 12.</span><span>Margherita</span><span>$ 12.</span><span>Chicken supreme</span><span>$ 12.</span><span>Chicken supreme</span><span>$ 12.</span><span>Beef Pizza</span><span>$ 12.</span><span>Beef Pizza</span><span>$ 12.</span><span>Margherita</span><span>$ 12.</span><span>Margherita</span><span>$ 12.</span></div></div>
    <div class="menu-section" style="top:158px"><div class="menu-section__head" style="background:var(--red)">Choose your salad</div>
      <div class="items items--grey"><span>Beef Pizza</span><span>$ 12.</span><span>Beef Pizza</span><span>$ 12.</span><span>Margherita</span><span>$ 12.</span><span>Margherita</span><span>$ 12.</span><span>Chicken supreme</span><span>$ 12.</span><span>Chicken supreme</span><span>$ 12.</span><span>Beef Pizza</span><span>$ 12.</span><span>Beef Pizza</span><span>$ 12.</span><span>Margherita</span><span>$ 12.</span><span>Margherita</span><span>$ 12.</span></div></div>
    <div class="menu-section" style="top:230px"><div class="menu-section__head" style="background:var(--red)">Choose your pasta</div>
      <div class="items items--grey"><span>Beef Pizza</span><span>$ 12.</span><span>Beef Pizza</span><span>$ 12.</span><span>Margherita</span><span>$ 12.</span><span>Margherita</span><span>$ 12.</span><span>Chicken supreme</span><span>$ 12.</span><span>Chicken supreme</span><span>$ 12.</span><span>Beef Pizza</span><span>$ 12.</span><span>Beef Pizza</span><span>$ 12.</span><span>Margherita</span><span>$ 12.</span><span>Margherita</span><span>$ 12.</span></div></div>
    <div class="menu-section" style="top:300px"><div class="menu-section__head" style="background:var(--red)">Choose your pasta</div>
      <div class="items items--grey"><span>Beef Pizza</span><span>$ 12.</span><span>Beef Pizza</span><span>$ 12.</span><span>Margherita</span><span>$ 12.</span><span>Margherita</span><span>$ 12.</span><span>Chicken supreme</span><span>$ 12.</span><span>Chicken supreme</span><span>$ 12.</span><span>Beef Pizza</span><span>$ 12.</span><span>Beef Pizza</span><span>$ 12.</span><span>Margherita</span><span>$ 12.</span><span>Margherita</span><span>$ 12.</span><span>Beef Pizza</span><span>$ 12.</span><span>Beef Pizza</span><span>$ 12.</span><span>Margherita</span><span>$ 12.</span><span>Margherita</span><span>$ 12.</span><span>Chicken supreme</span><span>$ 12.</span><span>Chicken supreme</span><span>$ 12.</span><span>Beef Pizza</span><span>$ 12.</span><span>Beef Pizza</span><span>$ 12.</span><span>Margherita</span><span>$ 12.</span><span>Margherita</span><span>$ 12.</span></div></div>
    <div class="menu-section" style="top:407px"><div class="menu-section__head" style="background:var(--red)">Choose your pasta</div>
      <div class="items items--grey"><span>Beef Pizza</span><span>$ 12.</span><span>Beef Pizza</span><span>$ 12.</span><span>Margherita</span><span>$ 12.</span><span>Margherita</span><span>$ 12.</span><span>Chicken supreme</span><span>$ 12.</span><span>Chicken supreme</span><span>$ 12.</span><span>Beef Pizza</span><span>$ 12.</span><span>Beef Pizza</span><span>$ 12.</span><span>Margherita</span><span>$ 12.</span><span>Margherita</span><span>$ 12.</span></div></div>
    <div class="logo-box" style="left:17px;top:478px;width:75px;height:80px;background:#fff;color:var(--ink);font-size:11px;padding:4px">Ironstone Brewhouse</div>
    <div class="photo" role="img" aria-label="Salad bowl" style="left:92px;top:478px;width:96px;height:80px;background:linear-gradient(135deg,#e8e2d4,#7a8a3a 60%,#b0502a)"></div>
    <div class="photo" role="img" aria-label="Burger topped with onion strings" style="left:188px;top:478px;width:96px;height:80px;background:linear-gradient(135deg,#c08a4a,#6a3a1a 60%,#2a1a10)"></div>
  </div>

  <!-- Restaurant panel: Marlow's Steak House -->
  <div class="panel panel--right">
    <div class="photo" role="img" aria-label="Grilled steak with asparagus" style="left:0;top:0;width:289px;height:112px;background:linear-gradient(120deg,#e6c08a,#6a2a14 45%,#3a1a0e 70%,#d8c8a8)"></div>
    <div class="photo" role="img" aria-label="Grilled meat skewers" style="left:0;top:112px;width:97px;height:64px;background:linear-gradient(135deg,#3a1a10,#9a4a22)"></div>
    <div class="photo" role="img" aria-label="Plate of pasta" style="left:97px;top:112px;width:110px;height:64px;background:linear-gradient(135deg,#4a2a1a,#b8542a 60%,#f0e6da)"></div>
    <div class="logo-box" style="left:211px;top:112px;width:62px;height:64px;background:#111;color:#d8b25a;font-size:10px;padding:3px">Marlow's Steak House</div>
    <div style="position:absolute;left:0;top:176px;width:289px;height:350px;background:var(--dark)"></div>
    <h2 class="menu-title menu-title--grey" style="top:190px">Choose your menu</h2>
    <div class="menu-section" style="top:220px"><div class="menu-section__head" style="background:var(--deep-red)">Choose your pizza</div>
      <div class="items items--grey"><span>Beef Pizza</span><span>$ 12.</span><span>Beef Pizza</span><span>$ 12.</span><span>Margherita</span><span>$ 12.</span><span>Margherita</span><span>$ 12.</span><span>Chicken supreme</span><span>$ 12.</span><span>Chicken supreme</span><span>$ 12.</span><span>Beef Pizza</span><span>$ 12.</span><span>Beef Pizza</span><span>$ 12.</span><span>Margherita</span><span>$ 12.</span><span>Margherita</span><span>$ 12.</span></div></div>
    <div class="menu-section" style="top:287px"><div class="menu-section__head" style="background:var(--deep-red)">Choose your pasta</div>
      <div class="items items--grey"><span>Beef Pizza</span><span>$ 12.</span><span>Beef Pizza</span><span>$ 12.</span><span>Margherita</span><span>$ 12.</span><span>Margherita</span><span>$ 12.</span><span>Chicken supreme</span><span>$ 12.</span><span>Chicken supreme</span><span>$ 12.</span><span>Beef Pizza</span><span>$ 12.</span><span>Beef Pizza</span><span>$ 12.</span><span>Margherita</span><span>$ 12.</span><span>Margherita</span><span>$ 12.</span></div></div>
    <div class="menu-section" style="top:359px"><div class="menu-section__head" style="background:var(--deep-red)">Choose your pasta</div>
      <div class="items items--grey"><span>Beef Pizza</span><span>$ 12.</span><span>Beef Pizza</span><span>$ 12.</span><span>Margherita</span><span>$ 12.</span><span>Margherita</span><span>$ 12.</span><span>Chicken supreme</span><span>$ 12.</span><span>Chicken supreme</span><span>$ 12.</span><span>Beef Pizza</span><span>$ 12.</span><span>Beef Pizza</span><span>$ 12.</span><span>Margherita</span><span>$ 12.</span><span>Margherita</span><span>$ 12.</span></div></div>
    <div class="menu-section" style="top:429px"><div class="menu-section__head" style="background:var(--deep-red)">Choose your pasta</div>
      <div class="items items--grey"><span>Beef Pizza</span><span>$ 12.</span><span>Beef Pizza</span><span>$ 12.</span><span>Margherita</span><span>$ 12.</span><span>Margherita</span><span>$ 12.</span><span>Chicken supreme</span><span>$ 12.</span><span>Chicken supreme</span><span>$ 12.</span><span>Beef Pizza</span><span>$ 12.</span><span>Beef Pizza</span><span>$ 12.</span><span>Margherita</span><span>$ 12.</span><span>Margherita</span><span>$ 12.</span></div></div>
    <div style="position:absolute;left:0;top:526px;width:289px;height:32px;background:#fff;display:flex;align-items:center;justify-content:center">
      <p class="call-line" style="color:var(--ink)"><b>CALL NOW</b> (555) 0 food now (555) 010-2468</p>
    </div>
  </div>
</section>

</body>
</html>
```